Bag cardboard

Hi,

We are a language school, We want to provide our students with a bag cardboard each time they suscribe for a language course.

You can find in the attachement a pictutre of our current model.

For the new one, we want 3 logos to be included. (you can find in the attachement the 3 logos).

We also want our 3 adresses to be included in the model
Tunis - Imm Les Amandiers, 2ème étage 47 Rue du Lac Malawi, 1082 Les Rives du Parc 2
(phone logo) 71 482 613
(Email logo) tunis@parlomo.org

Sfax - Imm Yasmina, 4ème étage Rue Hedi Mbarki (en face de la poste), 3041 Sfax
(phone logo) 74 718 152
(email logo) sfax@parlomo.org

Sousse - 52 Ave Khalil Mardam (prés du rond point Belvédère au dessus du café Jasmin).
(phone logo) 73 594 206
(email logo) sousse@parlomo.org

The website needs to be cited also :
www.parlomo.org

And also the SOCIALIA Page
(SOCIALIA logo) /PARLOMO

Waiting for your suggestions !

Thx

```html
<!DOCTYPE html>
<html lang="fr">
<head>
<meta charset="utf-8">
<title>Parlomo Centre – sac cartonné</title>
<link rel="stylesheet" href="https://fonts.googleapis.com/css2?family=Oswald:wght@400;500;600&display=swap">
<style>
  :root {
    --bg-top: #b3b2b3;
    --bg-bottom: #f2f2f2;
    --panel-black: #020202;
    --accent-yellow: #dadc14;
    --band-light: #e3e3e3;
    --ink: #1a1a1a;
    --ink-soft: #3a3a3a;
    --white: #f1f1f1;
    --partner-teal: #2f9a8a;
    --partner-brown: #6b5a2a;
  }
  * { box-sizing: border-box; margin: 0; padding: 0; }
  html, body { width: 1200px; height: 1200px; overflow: hidden; }
  body {
    background: linear-gradient(180deg, var(--bg-top) 0%, var(--bg-bottom) 100%);
    font-family: "Oswald", "Arial Narrow", sans-serif;
    position: relative;
  }
  .bag-face {
    position: absolute;
    left: 250px; top: 130px;
    width: 700px; height: 940px;
    background: var(--band-light);
    box-shadow: 0 6px 24px rgba(0,0,0,.12);
  }
  .brand-panel {
    position: absolute; left: 0; top: 0;
    width: 100%; height: 700px;
    background: var(--panel-black);
    border-left: 14px solid var(--accent-yellow);
  }
  .brand-name {
    position: absolute;
    left: 90px; top: 250px;
    color: var(--white);
    font-weight: 500;
    line-height: .9;
    letter-spacing: -2px;
  }
  .brand-name .word-main { display: block; font-size: 168px; }
  .brand-name .word-sub { display: block; font-size: 96px; text-align: right; margin-top: 4px; }
  .info-band {
    position: absolute; left: 0; top: 700px;
    width: 100%; height: 240px;
    padding: 28px 34px 0;
  }
  .addresses { display: flex; gap: 34px; }
  .address {
    width: 190px;
    font-size: 9.5px; line-height: 1.3;
    text-transform: uppercase;
    color: var(--ink-soft);
    font-weight: 500;
  }
  .address .city { font-weight: 600; color: var(--ink); }
  .partners {
    position: absolute; left: 34px; bottom: 42px;
    display: flex; gap: 36px; align-items: center;
  }
  .partner { display: flex; align-items: center; gap: 7px; font-size: 15px; font-weight: 500; }
  .partner-mark { width: 16px; height: 16px; }
  .partner--vallora { color: var(--partner-teal); }
  .partner--vallora .partner-mark { background: var(--partner-teal); }
  .partner--mirento { color: var(--partner-brown); }
  .partner--mirento .partner-mark { background: var(--partner-brown); border-radius: 50%; }
  .web-links {
    position: absolute; right: 34px; bottom: 40px;
    text-align: left;
    color: var(--ink);
    letter-spacing: 3px;
    font-weight: 500;
  }
  .web-links .site { font-size: 19px; padding-bottom: 6px; border-bottom: 1px solid var(--ink); }
  .web-links .social { font-size: 19px; padding-top: 6px; }
</style>
</head>
<body>
  <main class="bag-face">
    <section class="brand-panel">
      <h1 class="brand-name"><span class="word-main">parlomo</span><span class="word-sub">centre</span></h1>
    </section>
    <section class="info-band">
      <div class="addresses">
        <p class="address"><span class="city">Tunis –</span> Imm Les Amandiers, 2ème étage 47 Rue du Lac Malawi, 1082 Les Rives du Parc 2<br>71 482 613<br>tunis@parlomo.org</p>
        <p class="address"><span class="city">Sfax –</span> Imm Yasmina, 4ème étage Rue Hedi Mbarki (en face de la poste), 3041 Sfax<br>74 718 152<br>sfax@parlomo.org</p>
        <p class="address"><span class="city">Sousse –</span> 52 Ave Khalil Mardam (prés du rond point Belvédère au dessus du café Jasmin)<br>73 594 206<br>sousse@parlomo.org</p>
      </div>
      <div class="partners">
        <div class="partner partner--vallora"><span class="partner-mark"></span>VALLORA</div>
        <div class="partner partner--mirento"><span class="partner-mark"></span>mirento</div>
      </div>
      <div class="web-links">
        <p class="site">WWW.PARLOMO.ORG</p>
        <p class="social">SOCIALIA /PARLOMO</p>
      </div>
    </section>
  </main>
</body>
</html>
```